Bramwell Builders Web Site / Business Cards

Construction Company that specializes in Water and Fire Damage, Residential ReModels, Landscaping and Building ADU (Accessory Dwelling Unit)

Growing and changing families often need additional space, and a remodeling project can often provide that. Adding a new area, or repurposing an existing one can satisfy this requirement.

Other times, homeowners want to update the look in their kitchen or bathroom with more than just a change of cabinetry or vanity doors and drawers. Whatever your needs are, Bramwell Builders has skilled workers who are bonded and insured, and ready to make your dreams and visions a reality.

Target Market(s)

Home Owners

Industry/Entity Type

Construction Company

Contact Information for Business Card

Center Logo with our information on the corners

Back side to be Logo Only
Contact Info
SBRQ License # 5820914
info@bramwellbuildersca.example
www.bramwellbuildersca.example

Coding

Coded - Design and coding required

Number of Pages Required

5+ page

Font styles to use
Serif
Sans Serif

Requirements
Must have
• Using our Logo Colors
Home
About Us
Services
Projects / Portfolio
Contact Us
Nice to have
• Colors matching our Logo
Should not have
• Black because it doesnt match our logo

```html
<!DOCTYPE html>
<html lang="en">
<head>
<meta charset="utf-8">
<title>Bramwell Builders — Construction Services</title>
<link href="https://fonts.googleapis.com/css2?family=Open+Sans:ital,wght@0,400;0,600;0,700;0,800;1,400&display=swap" rel="stylesheet">
<style>
:root{
  --orange:#ff6a00;
  --deep:#4a2a16;
  --ink:#3b322c;
  --text:#4d4741;
  --muted:#6e6760;
  --paper:#ffffff;
  --mist:#efefef;
  --card-a:#6a5648;
  --card-b:#4f3d31;
}
*{box-sizing:border-box;margin:0;padding:0}
html,body{width:1200px;height:4521px;overflow:hidden}
body{position:relative;background:var(--paper);font-family:"Open Sans",Arial,sans-serif;color:var(--text)}
.abs{position:absolute}

/* header */
.site-header{left:0;top:0;width:1200px;height:79px;background:var(--paper)}
.brand-box{left:49px;top:0;width:136px;height:132px;background:var(--paper);box-shadow:0 2px 6px rgba(0,0,0,.2);display:flex;flex-direction:column;align-items:center;justify-content:center;gap:8px;z-index:5}
.brand-square{width:28px;height:28px;background:var(--orange)}
.brand-name{font-weight:800;font-size:17px;line-height:1.1;color:var(--ink);text-align:center;letter-spacing:.5px}
.nav{left:320px;top:0;height:79px;display:flex}
.nav a{font-size:15px;color:var(--ink);text-decoration:none;line-height:79px;margin-right:46px;position:relative}
.nav a.active{color:var(--orange)}
.nav a.active::after{content:"";position:absolute;left:-6px;right:-6px;bottom:0;height:3px;background:var(--orange)}
.header-tools{left:839px;top:0;width:361px;height:79px;background:#ebe8e5}
.phone-chip{left:869px;top:22px;width:36px;height:36px;background:var(--orange);border-radius:3px}
.phone-num{left:914px;top:29px;font-size:14px;color:var(--ink);font-weight:600}
.quote-btn{left:1042px;top:23px;width:123px;height:35px;background:var(--orange);color:#fff;font-size:13px;display:flex;align-items:center;justify-content:center}

/* hero */
.hero{left:0;top:79px;width:1200px;height:610px}
.hero-title{left:0;top:278px;width:1200px;text-align:center;color:#fff;font-weight:600;font-size:50px;line-height:1.2}
.hero-sub{left:0;top:350px;width:1200px;text-align:center;color:#fff;font-weight:700;font-size:28px;line-height:1.3}
.hero-btn{left:507px;top:432px;width:186px;height:47px;background:var(--orange);color:#fff;font-size:16px;font-weight:600;display:flex;align-items:center;justify-content:center}

/* section headings */
.section-head{display:flex;align-items:flex-end;gap:16px}
.head-mark{position:relative;width:120px;height:52px}
.head-mark::before{content:"";position:absolute;left:42px;top:0;width:44px;height:44px;background:var(--orange)}
.head-mark::after{content:"";position:absolute;left:0;bottom:0;width:120px;height:3px;background:var(--deep)}
.section-head h2{font-weight:600;font-size:26px;color:var(--ink);line-height:1;margin-bottom:12px;white-space:nowrap}

/* services */
.sketch-area{left:50px;top:690px;width:720px;height:520px;background:linear-gradient(180deg,#f5f3f1,#fbfaf9 70%,#fff)}
.service-card{width:310px;height:181px;background:linear-gradient(135deg,var(--card-a),var(--card-b))}
.service-card .icon{position:absolute;left:28px;top:22px;width:48px;height:48px}
.service-card .label{position:absolute;left:28px;bottom:22px;color:#fff;font-weight:600;font-size:22px;line-height:1.22}
.service-card .detail{display:block;font-size:13px;font-weight:400;margin-top:14px;padding-bottom:4px;border-bottom:1px solid var(--orange);width:max-content}

/* success */
.success{left:0;top:1416px;width:1200px;height:1100px;background:var(--mist)}
.feature .f-icon{position:absolute;left:0;top:0;width:62px;height:62px;border:3px solid var(--orange);background:#fff}
.feature h3{position:absolute;left:80px;top:16px;font-size:16px;font-weight:700;color:var(--ink);line-height:1.4;width:170px}
.feature p{position:absolute;left:0;top:86px;width:225px;font-size:13.5px;line-height:1.45;color:var(--muted)}
.deliver-title{left:0;top:1898px;width:1200px;text-align:center;font-size:19px;font-weight:600;color:var(--ink)}
.deliver-text{left:260px;top:1950px;width:680px;text-align:center;font-size:15px;line-height:1.6;color:var(--muted)}

/* stats */
.stat-num{font-size:66px;font-weight:800;color:var(--orange);line-height:1}
.stat-label{font-size:24px;font-weight:600;color:#fff;line-height:1;margin-top:-4px;white-space:nowrap}

/* recent projects */
.proj-orange{left:261px;top:2725px;width:439px;height:390px;background:var(--orange)}
.proj-accent{left:65px;top:3062px;width:128px;height:129px;background:var(--deep)}
.proj-photo{left:81px;top:2740px;width:598px;height:431px;background:linear-gradient(180deg,#a9cbe8 0%,#dfe9f1 40%,#d7d2c8 62%,#67b6c9 78%,#7bb258 100%)}
.proj-title{left:748px;top:2775px;font-size:27px;font-weight:600;color:var(--ink);line-height:1.02}
.proj-cats{left:748px;top:2852px;font-size:19px;font-weight:600;color:var(--orange)}
.proj-text{left:748px;top:2912px;width:370px;font-size:15px;line-height:1.48;color:var(--text)}
.proj-btn{left:748px;top:3126px;width:254px;height:65px;background:var(--orange);color:#fff;font-size:15px;font-weight:600;display:flex;align-items:center;justify-content:center}

/* testimonials */
.testimonials{left:0;top:3287px;width:1200px;height:780px;background:linear-gradient(180deg,#d6d3d0,#dddad7 60%,#e8e6e4)}
.quote-card{width:336px;height:219px;background:#eeeceb;padding:30px 24px 0 24px;font-size:15px;line-height:1.75;color:var(--text)}
.quote-card.italic{font-style:italic}
.quote-card::after{content:"";position:absolute;left:130px;bottom:-20px;border-left:20px solid transparent;border-top:20px solid #eeeceb}
.client{display:flex;align-items:center;gap:12px;font-size:15px;color:var(--ink)}
.avatar{width:48px;height:48px;border-radius:50%;background:linear-gradient(135deg,#9a8e85,#d6ceC8);border:2px solid #fff}

/* footer */
.foot-col h4{font-size:19px;font-weight:600;color:var(--ink);margin-bottom:16px}
.foot-col p{font-size:15px;line-height:1.75;color:var(--text)}
.foot-col b{font-weight:600;color:var(--ink)}
.foot-brand{left:490px;top:4098px;width:220px;display:flex;flex-direction:column;align-items:center;gap:12px}
.foot-brand .brand-square{width:40px;height:40px}
.foot-brand .brand-name{font-size:32px;letter-spacing:1px}
.socials{left:498px;top:4308px;display:flex;gap:28px}
.socials span{width:28px;height:28px;border-radius:50%;background:#7a706a}
.foot-rule{left:80px;top:4449px;width:1040px;height:1px;background:#dcd8d5}
.copyright{left:0;top:4472px;width:1200px;text-align:center;font-size:15px;color:var(--ink);font-weight:600}
</style>
</head>
<body>

<!-- header -->
<header class="abs site-header"></header>
<div class="abs brand-box"><span class="brand-square"></span><span class="brand-name">BRAMWELL<br>BUILDERS</span></div>
<nav class="abs nav">
  <a class="active" href="#">Home</a><a href="#">Company</a><a href="#">Projects</a><a href="#">Services</a><a href="#">Contact</a>
</nav>
<div class="abs header-tools"></div>
<div class="abs phone-chip">
  <svg width="36" height="36" viewBox="0 0 36 36"><path d="M12 10c1-1 2-1 3 0l2 3c.6 1 .3 1.8-.5 2.4l-1 .8c1 2.3 2.8 4 5 5l.8-1c.6-.8 1.4-1.1 2.4-.5l3 2c1 .7 1 2 0 3l-1.5 1.5c-1.5 1.3-4 1-7-1s-6-5-7.5-8.5c-1-2.5-.8-4.3.3-5.5z" fill="none" stroke="#fff" stroke-width="1.6"/></svg>
</div>
<div class="abs phone-num">+1 555 204 7781</div>
<div class="abs quote-btn">Get a Quote</div>

<!-- hero -->
<svg class="abs hero" viewBox="0 0 1200 610" role="img" aria-label="Photo of a two storey suburban house at dusk with lit windows and a driveway">
  <defs>
    <linearGradient id="heroSky" x1="0" y1="0" x2="0" y2="1">
      <stop offset="0" stop-color="#5d6270"/>
      <stop offset=".45" stop-color="#7a6f6a"/>
      <stop offset=".75" stop-color="#54504e"/>
      <stop offset="1" stop-color="#4a4645"/>
    </linearGradient>
  </defs>
  <polygon points="0,0 1200,0 1200,461 600,544 0,461" fill="url(#heroSky)"/>
  <polygon points="0,461 600,544 1200,461 1200,470 600,590 0,470" fill="var(--orange)"/>
  <polygon points="0,470 600,590 1200,470 1200,478 600,605 0,478" fill="var(--deep)"/>
</svg>
<div class="abs hero-title">Construction Services</div>
<div class="abs hero-sub">Creative &amp; professional service that your home needs</div>
<div class="abs hero-btn">Find Out More</div>

<!-- services -->
<div class="abs sketch-area" role="img" aria-label="Faint architectural line drawing of a modern house"></div>
<div class="abs section-head" style="left:360px;top:750px"><span class="head-mark"></span><h2>What Can We Help You With?</h2></div>

<div class="abs service-card" style="left:81px;top:897px" role="img" aria-label="Home construction interior photo">
  <svg class="icon" viewBox="0 0 48 48"><path d="M6 22 24 8l18 14M11 19v21h26V19M20 40V29h8v11" fill="none" stroke="var(--orange)" stroke-width="2.4"/></svg>
  <div class="label">Home<br>Constructions<span class="detail">View Detail</span></div>
</div>
<div class="abs service-card" style="left:446px;top:897px" role="img" aria-label="Residential remodeling photo">
  <svg class="icon" viewBox="0 0 48 48"><rect x="7" y="7" width="34" height="34" fill="none" stroke="var(--orange)" stroke-width="2.4"/><path d="M13 35 35 13M28 13h7v7" fill="none" stroke="var(--orange)" stroke-width="2.4"/></svg>
  <div class="label">Residential<br>Remodeling</div>
</div>
<div class="abs service-card" style="left:809px;top:897px" role="img" aria-label="Water and fire damage restoration photo">
  <svg class="icon" viewBox="0 0 48 48"><path d="M17 8c5 8 9 13 9 18a9 9 0 0 1-18 0c0-5 4-10 9-18zM34 22c4 5 7 8 7 12a7 7 0 0 1-14 0c0-2 1-4 3-6 0 3 2 4 3 4 0-4 0-6 1-10z" fill="none" stroke="var(--orange)" stroke-width="2.4"/></svg>
  <div class="label">Water &amp; Fire<br>Damage</div>
</div>
<div class="abs service-card" style="left:81px;top:1128px" role="img" aria-label="Landscaped garden and pool photo">
  <svg class="icon" viewBox="0 0 48 48"><path d="M24 42V22M24 22c-10 0-14-8-14-14 8 0 14 4 14 14zM24 28c8 0 12-6 12-11-7 0-12 3-12 11M8 42h32" fill="none" stroke="var(--orange)" stroke-width="2.4"/></svg>
  <div class="label">Landscaping</div>
</div>
<div class="abs service-card" style="left:446px;top:1128px" role="img" aria-label="Renovation worker on a floor photo">
  <svg class="icon" viewBox="0 0 48 48"><rect x="8" y="8" width="26" height="10" fill="none" stroke="var(--orange)" stroke-width="2.4"/><path d="M34 13h6v10H22v6M20 29h4v13h-4z" fill="none" stroke="var(--orange)" stroke-width="2.4"/></svg>
  <div class="label">Renovation<br>Services</div>
</div>
<div class="abs service-card" style="left:809px;top:1128px" role="img" aria-label="Accessory dwelling unit photo">
  <svg class="icon" viewBox="0 0 48 48"><path d="M14 20 26 10l12 10v12H14zM6 40h10l8-6h10" fill="none" stroke="var(--orange)" stroke-width="2.4"/></svg>
  <div class="label">Accessory<br>Dwelling Unit (ADU)</div>
</div>

<!-- success -->
<div class="abs success"></div>
<div class="abs section-head" style="left:367px;top:1478px"><span class="head-mark"></span><h2>We Attribute Our Success to</h2></div>

<div class="abs feature" style="left:56px;top:1650px;width:260px;height:160px">
  <div class="f-icon"><svg width="56" height="56" viewBox="0 0 56 56"><circle cx="28" cy="24" r="11" fill="none" stroke="var(--ink)" stroke-width="2"/><path d="M28 18l2 4 4 .5-3 3 .8 4-3.8-2-3.8 2 .8-4-3-3 4-.5z" fill="none" stroke="var(--orange)" stroke-width="1.6"/><path d="M21 33l-3 12 5-2 3 4 2-8M35 33l3 12-5-2-3 4" fill="none" stroke="var(--ink)" stroke-width="2"/></svg></div>
  <h3>WE'VE REPUTION FOR EXCELLENCE</h3>
  <p>Lorem ipsum dolor sit amet, consectetur adipiscing elit, sed do eiusmod tempor incididunt ut labore et dolore magna aliqua.</p>
</div>
<div class="abs feature" style="left:347px;top:1650px;width:260px;height:160px">
  <div class="f-icon"><svg width="56" height="56" viewBox="0 0 56 56"><path d="M8 24l10-8 8 4 6-4 16 8M12 28l10 10c2 2 4 2 6 0l12-12M22 30l6 6M27 27l6 6" fill="none" stroke="var(--ink)" stroke-width="2"/></svg></div>
  <h3>WE BUILD PARTNERSHIPS</h3>
  <p>Lorem ipsum dolor sit amet, consectetur adipiscing elit, sed do eiusmod tempor incididunt ut labore et dolore magna aliqua.</p>
</div>
<div class="abs feature" style="left:627px;top:1650px;width:260px;height:160px">
  <div class="f-icon"><svg width="56" height="56" viewBox="0 0 56 56"><rect x="14" y="10" width="28" height="36" fill="none" stroke="var(--ink)" stroke-width="2"/><path d="M19 18h18M19 24h18M19 30h10" stroke="var(--ink)" stroke-width="2"/><circle cx="35" cy="37" r="5" fill="none" stroke="var(--orange)" stroke-width="2"/></svg></div>
  <h3>GUIDED BY COMMITMENT</h3>
  <p>Lorem ipsum dolor sit amet, consectetur adipiscing elit, sed do eiusmod tempor incididunt ut labore et dolore magna aliqua.</p>
</div>
<div class="abs feature" style="left:920px;top:1650px;width:260px;height:160px">
  <div class="f-icon"><svg width="56" height="56" viewBox="0 0 56 56"><path d="M18 46V30l-4-8 6-2 4 8V14l4 0v14l2-12 4 1-2 13 4-9 4 2-6 14v13" fill="none" stroke="var(--ink)" stroke-width="2"/><path d="M12 12l4 4M28 6v5M44 12l-4 4" stroke="var(--orange)" stroke-width="2"/></svg></div>
  <h3>A TEAM OF PROFESSIONALS</h3>
  <p>Lorem ipsum dolor sit amet, consectetur adipiscing elit, sed do eiusmod tempor incididunt ut labore et dolore magna aliqua.</p>
</div>

<div class="abs deliver-title">WE DELIVER LANDMARK PROJECTS</div>
<p class="abs deliver-text">We are rethoric question ran over her cheek When she reached the first hills of the Italic Mountains, she had a last view back on the skyline of her hometown Bookmarksgrove, the headline of Alphabet Village and the subline of her own road, the Line Lane.</p>

<!-- stats -->
<svg class="abs" style="left:0;top:2090px" width="1200" height="430" viewBox="0 0 1200 430">
  <polygon points="0,3 1200,85 1200,348 0,418" fill="var(--deep)"/>
</svg>
<div class="abs" style="left:67px;top:2265px"><div class="stat-num">53</div><div class="stat-label">TOTAL PROJECTS</div></div>
<div class="abs" style="left:340px;top:2265px"><div class="stat-num">371</div><div class="stat-label">STAFF MEMBERS</div></div>
<div class="abs" style="left:614px;top:2265px"><div class="stat-num">15</div><div class="stat-label">WORKING IN STATES</div></div>
<div class="abs" style="left:920px;top:2265px"><div class="stat-num">2600</div><div class="stat-label">HOURS FOR WORK</div></div>

<!-- recent projects -->
<div class="abs section-head" style="left:450px;top:2585px"><span class="head-mark"></span><h2>Recent Projects</h2></div>
<div class="abs proj-orange"></div>
<div class="abs proj-accent"></div>
<div class="abs proj-photo" role="img" aria-label="Photo of a modern villa with a swimming pool, patio umbrella and dining set"></div>
<svg class="abs" style="left:108px;top:2925px" width="30" height="60" viewBox="0 0 30 60"><path d="M26 4 4 30l22 26" fill="none" stroke="#fff" stroke-width="3" opacity=".8"/></svg>
<svg class="abs" style="left:620px;top:2925px" width="30" height="60" viewBox="0 0 30 60"><path d="M4 4l22 26L4 56" fill="none" stroke="#fff" stroke-width="3" opacity=".8"/></svg>
<div class="abs proj-title">New Custom Home<br>Canada</div>
<div class="abs proj-cats">Exterior Design, Renovation Services</div>
<p class="abs proj-text">Lorem ipsum dolor sit amet, consectetur adipiscing elit, sed do eiusmod tempor incididunt ut labore et dolore magna aliqua. Quis ipsum suspendisse ultrices gravida. Risus commodo viverra maecenas accumsan lacus vel facilisis. Lorem ipsum dolor sit amet, consectetur adipiscing elit, sed do eiusmod tempor incididunt</p>
<div class="abs proj-btn">Project Archive</div>

<!-- testimonials -->
<div class="abs testimonials" role="img" aria-label="Faded background photo of hands reviewing construction plans"></div>
<div class="abs section-head" style="left:328px;top:3358px"><span class="head-mark"></span><h2>What Our Customers Say About Us</h2></div>

<div class="abs quote-card italic" style="left:65px;top:3489px">BramwellBuilders is one of the best general contractors we've worked with. The entire team tactfully delivered a project of exceptional quality while staying on schedule and under budget. We hope to work with Bramwell again in the near future!</div>
<div class="abs quote-card" style="left:433px;top:3489px">Lorem ipsum dolor sit amet, consectetur adipiscing elit, sed do eiusmod tempor incididunt ut labore et dolore magna aliqua. Quis ipsum suspendisse ultrices gravida. Risus commodo viverra maecenas accumsan lacus vel facilisis.</div>
<div class="abs quote-card" style="left:802px;top:3489px">Lorem ipsum dolor sit amet, consectetur adipiscing elit, sed do eiusmod tempor incididunt ut labore et dolore magna aliqua. Quis ipsum suspendisse ultrices gravida. Risus commodo viverra maecenas accumsan lacus vel facilisis.</div>

<div class="abs client" style="left:241px;top:3725px"><span class="avatar" role="img" aria-label="Client portrait"></span>Marla Finch</div>
<div class="abs client" style="left:610px;top:3725px"><span class="avatar" role="img" aria-label="Client portrait"></span>John Doe</div>
<div class="abs client" style="left:978px;top:3725px"><span class="avatar" role="img" aria-label="Client portrait"></span>Smith T.</div>

<!-- roof divider and footer -->
<svg class="abs" style="left:0;top:3910px" width="1200" height="160" viewBox="0 0 1200 160">
  <polygon points="0,132 600,0 1200,132 1200,142 600,22 0,142" fill="var(--deep)"/>
  <polygon points="120,116 600,22 1080,116 1080,126 600,50 120,126" fill="var(--orange)"/>
  <polygon points="0,142 600,22 1200,142 1200,160 0,160" fill="#fff"/>
  <polygon points="120,116 600,22 1080,116 1080,126 600,48 120,126" fill="var(--orange)"/>
</svg>

<div class="abs foot-col" style="left:86px;top:4114px;width:320px">
  <h4>Working Hours</h4>
  <p>we work 7 days a week, every day excluding major holidays. contact us if you have an emergency, with our hotline and contact form.<br><b>monday – friday:10:00 – 16:00</b><br><b>saturday:12:00 – 15:00</b><br><b>sunday and holidays:09:00 – 12:00</b></p>
</div>

<div class="abs foot-brand"><span class="brand-square"></span><span class="brand-name">BRAMWELL</span><span class="brand-name" style="font-size:20px;margin-top:-10px">BUILDERS</span></div>
<div class="abs socials"><span aria-label="Social link"></span><span aria-label="Social link"></span><span aria-label="Social link"></span><span aria-label="Social link"></span></div>

<div class="abs foot-col" style="left:760px;top:4114px;width:360px;text-align:right">
  <h4>Contact us</h4>
  <p><b>Dalton R Severin</b> | Branch Manager<br><b>Office :</b> 555-204-7781<br><b>Direct :</b> 555-318-6620<br><b>Fax :</b> 555-204-7790<br><b>dsevern@bramwellbuildersca.example</b><br>412 W Orchard Row Fairhaven<br>CA 90999</p>
</div>

<div class="abs foot-rule"></div>
<div class="abs copyright">Copyright © 2020 BRAMWELL Builders</div>

</body>
</html>
```